We want to change our offer process. Customers will receive a link by email to a landing page, which shows the offer we created for them.
We quickly build a landing page with all the elements, which should also be in the final version, but the design is just random and only to show the idea. Please design us a landing page which looks much more attractive and state of the art.
Please note that under the offered items, there should be a slider with similar products. We are sending you the demo landing page. The colors should match our main web shop: kaminwerk-versand.de
Target Market(s)
Customers from 45yr. of age; homeowner
Industry/Entity Type
Stoves, fireplaces and chimney
Number of Pages Required
1 page
Look and feel

```html
<!DOCTYPE html>
<html lang="de">
<head>
<meta charset="utf-8">
<title>Angebot Nr. 128471 – Kaminwerk Versand</title>
<link href="https://fonts.googleapis.com/css2?family=Poppins:wght@400;500;600;700&display=swap" rel="stylesheet">
<style>
:root{
  --orange:#f0a83a;
  --orange-dark:#e08d16;
  --orange-soft:#fdf1de;
  --yellow:#f7d37c;
  --ink:#2b2b2b;
  --muted:#777;
  --line:#e3e3e3;
  --panel:#f3f3f3;
  --dark:#1f1f1f;
  --dark-2:#2c2c2c;
  --red:#d73a2e;
  --badge:#3c6eb4;
  --white:#fff;
}
*{box-sizing:border-box;margin:0;padding:0}
html,body{width:1200px;height:3524px;overflow:hidden}
body{font-family:"Poppins",Arial,sans-serif;color:var(--ink);background:var(--white);position:relative}
a{color:inherit}

/* header */
.site-header{height:150px;border-bottom:1px solid var(--line);position:relative}
.brand{position:absolute;left:36px;top:14px;display:flex;align-items:center;gap:10px;font-weight:700;font-size:17px;color:var(--orange-dark);line-height:1.1;text-transform:uppercase}
.brand-mark{width:28px;height:28px;border-radius:50%;background:var(--orange)}
.search{position:absolute;left:410px;top:18px;width:330px;height:34px;border:1px solid var(--line);border-radius:18px;font-size:12px;color:#aaa;padding:8px 18px}
.search svg{position:absolute;right:12px;top:9px}
.hotline{position:absolute;right:36px;top:12px;text-align:right;line-height:1.3}
.hotline b{display:block;color:var(--orange-dark);font-size:17px}
.hotline span{font-size:10px;color:var(--muted)}
.header-icons{position:absolute;right:36px;top:66px;display:flex;gap:10px}
.header-icons i{width:22px;height:22px;border-radius:50%;background:var(--orange);display:block}
.main-nav{position:absolute;left:36px;top:100px;display:flex;gap:40px;font-size:13px;font-weight:500}
.main-nav .usp{color:var(--orange-dark);font-size:12px}

/* offer heading */
.offer-title{text-align:center;color:var(--orange-dark);font-size:38px;font-weight:700;margin-top:46px}

.address-row{position:relative;height:340px}
.address-card{position:absolute;top:28px;background:var(--orange);color:var(--white);padding:26px 28px;border-radius:4px;box-shadow:0 6px 16px rgba(224,141,22,.25)}
.address-card h2{font-size:24px;line-height:1.2;margin-bottom:18px}
.address-card p{font-size:13px;line-height:1.75}
.card-buyer{left:124px;width:288px;height:300px}
.card-delivery{left:444px;width:300px;height:300px}
.card-billing{left:776px;width:330px;height:200px}

/* items table */
.items{margin:36px 48px 0;width:1104px;border-collapse:collapse;font-size:12px}
.items th{background:var(--orange);color:var(--white);text-align:left;padding:10px 10px;font-weight:600}
.items td{padding:14px 10px;border-bottom:1px solid var(--line);border-right:1px solid var(--line)}
.items td:first-child{border-left:1px solid var(--line)}

.totals{margin:22px 48px 0 auto;width:440px;font-size:13px;border-collapse:collapse}
.totals td{padding:11px 16px;border:1px solid var(--line)}
.totals tr:first-child td{background:var(--orange);color:var(--white);font-weight:600}
.totals td:last-child{text-align:right;font-weight:700}

.offer-notes{text-align:center;font-size:15px;line-height:1.75;margin-top:30px;font-weight:500}

/* payment panel */
.payment-panel{margin:66px 80px 0 112px;width:1008px;height:560px;background:var(--panel);position:relative}
.pay-box{position:absolute;left:28px;top:32px;width:420px;height:490px;background:var(--white);padding:30px 34px;text-align:center}
.pay-amount{border:2px solid var(--orange);border-radius:6px;padding:14px;font-size:28px;font-weight:700}
.pay-amount span{color:var(--orange-dark)}
.pay-info{font-size:12px;color:var(--muted);line-height:1.7;margin:20px 0 24px}
.btn{display:block;height:72px;border-radius:6px;font-size:18px;font-weight:600;line-height:72px;margin-bottom:18px}
.btn-submit{background:var(--yellow);color:var(--ink)}
.btn-pdf{background:#4a4a4a;color:var(--white)}
.pay-link{font-size:10px;color:var(--orange-dark);text-decoration:underline}
.pay-methods{display:flex;justify-content:space-between;margin-top:14px;font-size:10px;color:#555;font-weight:600}

.doc-list{position:absolute;left:500px;top:36px;list-style:none;font-size:11.5px;line-height:1}
.doc-list li{display:flex;align-items:center;gap:10px;margin-bottom:13px}
.doc-list li a{text-decoration:underline}
.pdf-icon{width:14px;height:16px;background:var(--red);border-radius:2px;flex:none}

/* trust band */
.trust-band{margin-top:100px;height:260px;background:var(--dark);color:var(--white);position:relative}
.trust-list{position:absolute;top:30px;list-style:none;font-size:15px;font-weight:600;line-height:1.3}
.trust-list li{display:flex;gap:10px;margin-bottom:12px}
.trust-list li svg{flex:none;margin-top:2px}
.trust-left{left:40px;width:330px}
.trust-right{left:800px;width:370px}
.trust-right small{display:block;font-weight:400;font-size:13px}
.trust-right small b{color:var(--orange)}
.best-price{position:absolute;left:40px;top:186px;background:var(--orange-dark);color:var(--white);font-weight:700;font-size:20px;padding:8px 18px;letter-spacing:.5px}
.badges{position:absolute;left:420px;top:24px;width:340px;height:210px}
.badge-round{position:absolute;top:0;width:92px;height:92px;border-radius:50%;background:var(--badge);border:6px solid var(--white)}
.badge-round:nth-child(1){left:0}
.badge-round:nth-child(2){left:116px}
.badge-wide{position:absolute;left:100px;top:124px;width:170px;height:64px;background:var(--white);border-radius:6px}

/* company info */
.company-info{display:grid;grid-template-columns:repeat(4,1fr);gap:20px;padding:60px 90px 0;height:320px}
.company-info h3{font-size:17px;margin-bottom:16px}
.company-info p{font-size:11px;color:var(--muted);line-height:1.9}

/* similar products slider */
.similar{background:var(--orange);height:620px;position:relative}
.tabs{position:absolute;left:180px;top:40px;display:flex}
.tab{width:420px;height:54px;line-height:54px;text-align:center;font-weight:600;font-size:16px}
.tab-active{background:#d98a1c;color:var(--white)}
.tab-idle{background:var(--orange-soft);color:var(--orange-dark)}
.slide{position:absolute;left:120px;top:130px;width:960px;height:420px}
.slide-image{position:absolute;left:0;top:0;width:440px;height:400px;background:linear-gradient(160deg,#ffffff,#e9e9e9);border-radius:4px}
.slide-text{position:absolute;left:480px;top:20px;width:470px;color:var(--white)}
.slide-text h3{font-size:26px;margin-bottom:18px}
.slide-text p{font-size:11px;line-height:1.8}
.dots{position:absolute;left:250px;top:580px;display:flex;gap:8px}
.dots i{width:32px;height:5px;background:rgba(255,255,255,.55);display:block}
.dots i:first-child{background:var(--white)}

/* footer */
.site-footer{background:var(--dark-2);color:#ddd;height:484px;position:relative;font-size:11px}
.footer-head{position:absolute;top:30px;font-size:16px;font-weight:600;color:var(--white)}
.pay-head{left:60px}.ship-head{right:60px}
.logo-row{position:absolute;top:70px;display:flex;gap:22px;font-weight:600;color:var(--white)}
.logo-row span{display:flex;align-items:center;gap:6px}
.logo-row span::before{content:"";width:8px;height:8px;background:var(--orange);display:block}
.pay-row{left:60px}.ship-row{right:60px}
.footer-divider{position:absolute;left:60px;right:60px;top:112px;border-top:1px solid #444}
.footer-cols{position:absolute;left:60px;top:140px;display:flex;gap:110px}
.footer-cols ul{list-style:none;line-height:1.9}
.support{position:absolute;left:60px;top:300px;color:var(--orange);font-weight:600;font-size:14px}
.footer-contact{position:absolute;right:60px;top:140px;text-align:right;line-height:1.9}
.footer-contact b{color:var(--white)}
.copyright{position:absolute;left:0;right:0;bottom:0;height:40px;background:var(--dark);text-align:right;padding:12px 60px;font-size:10px;color:#999}
</style>
</head>
<body>

<header class="site-header">
  <div class="brand"><span class="brand-mark"></span><span>Kaminwerk<br>Versand</span></div>
  <div class="search">Suche nach Artikeln &hellip;
    <svg width="16" height="16" viewBox="0 0 16 16"><circle cx="7" cy="7" r="5" fill="none" stroke="#e08d16" stroke-width="2"/><line x1="11" y1="11" x2="15" y2="15" stroke="#e08d16" stroke-width="2"/></svg>
  </div>
  <div class="hotline"><b>&#9742; 089 4521 3370</b><span>Mo–Fr 8–18 Uhr</span></div>
  <div class="header-icons"><i></i><i></i><i></i></div>
  <nav class="main-nav">
    <span>Online shop ▾</span><span>service ▾</span><span class="usp">✓ Kostenloser Versand ab 100 €</span>
  </nav>
</header>

<main>
  <h1 class="offer-title">Angebot Nr. 128471</h1>

  <section class="address-row">
    <div class="address-card card-buyer">
      <h2>Käufer:</h2>
      <p>Lukas Brenner<br>Lindenweg 12<br>80331 München<br>GERMANY</p>
    </div>
    <div class="address-card card-delivery">
      <h2>Lieferadresse des Käufers:</h2>
      <p>Lukas Brenner<br>Birkenstraße 4<br>10115 Berlin<br>GERMANY</p>
    </div>
    <div class="address-card card-billing">
      <h2>Rechnungs-Details:</h2>
      <p>Bearbeiter: Test Kontoname<br>Kunden-Nr.: 225027<br>Datum: 2024-03-22 10:14:59</p>
    </div>
  </section>

  <table class="items">
    <thead>
      <tr><th>Pos</th><th>Bezeichnung</th><th>ID</th><th>Delivery time</th><th>Anz</th><th>USt</th><th>Brutto Preis</th><th>Brutto Gesamt</th></tr>
    </thead>
    <tbody>
      <tr><td>1</td><td>Kaminofen Brennwald Aurum 8 kW</td><td>8</td><td>07</td><td>1</td><td>19%</td><td>318,99 €</td><td>318,99 €</td></tr>
      <tr><td>2</td><td>Kaminofen Brennwald Solvik K+ 2.0 11 kW</td><td>8</td><td>07</td><td>1</td><td>19%</td><td>3.112,10 €</td><td>3.112,10 €</td></tr>
    </tbody>
  </table>

  <table class="totals">
    <tr><td>Gesamtkosten Netto:</td><td>2.779,98 €</td></tr>
    <tr><td>zzgl. 19% USt:</td><td>547,82 €</td></tr>
    <tr><td>Gesamtkosten:</td><td>3.431,09 €</td></tr>
  </table>

  <p class="offer-notes">Gewählte Versandart: Standardversand DE test<br>Angebot freibleibend. Änderung der Tagespreise möglich.<br>Vielen herzlichen Dank für Ihre Anfrage bei kaminwerk-versand.de.</p>

  <section class="payment-panel">
    <div class="pay-box">
      <div class="pay-amount">Sie zahlen : <span>3.431,09€</span></div>
      <p class="pay-info">inkl. MwSt und Versandkosten<br>Sie sparen 98,94 € gegenüber dem Einzelkauf</p>
      <a class="btn btn-submit">Submit</a>
      <a class="btn btn-pdf">Send Pdf</a>
      <a class="pay-link">Vorauskasse Informationen</a>
      <div class="pay-methods"><span>Lastschrift</span><span>Kreditkarte</span><span>Sofortkauf</span><span>Vorkasse</span><span>Rechnung</span></div>
    </div>
    <ul class="doc-list">
      <li><i class="pdf-icon"></i><a>Benutzerhandbuch Kaminofen Brennwald Aurum</a></li>
      <li><i class="pdf-icon"></i><a>Leistungserklärung Kaminofen Brennwald Aurum</a></li>
      <li><i class="pdf-icon"></i><a>Energie Label Kaminofen Brennwald Aurum</a></li>
      <li><i class="pdf-icon"></i><a>Produkt Datenblatt Kaminofen Brennwald Aurum</a></li>
      <li><i class="pdf-icon"></i><a>Datenblatt Kaminofen Brennwald Aurum</a></li>
      <li><i class="pdf-icon"></i><a>Benutzerhandbuch Kaminofen Brennwald Solvik K+20</a></li>
      <li><i class="pdf-icon"></i><a>Leistungserklärung Kaminofen Brennwald Solvik K+20</a></li>
      <li><i class="pdf-icon"></i><a>Energie Label Kaminofen Brennwald Solvik K+2.0</a></li>
      <li><i class="pdf-icon"></i><a>Produkt Datenblatt Kaminofen Brennwald Solvik K+2.0</a></li>
      <li><i class="pdf-icon"></i><a>New description 2</a></li>
      <li><i class="pdf-icon"></i><a>New description</a></li>
      <li><i class="pdf-icon"></i><a>BRENNWALD Kaminofen Solvik K+20</a></li>
      <li><i class="pdf-icon"></i><a>Montage Dreh-Tableau BRENNWALD Kaminofen</a></li>
    </ul>
  </section>

  <section class="trust-band">
    <ul class="trust-list trust-left">
      <li><svg width="16" height="16" viewBox="0 0 16 16"><circle cx="8" cy="8" r="8" fill="#e08d16"/><path d="M4 8l3 3 5-6" stroke="#fff" stroke-width="2" fill="none"/></svg>Markenhändler mit Zertifizierung</li>
      <li><svg width="16" height="16" viewBox="0 0 16 16"><circle cx="8" cy="8" r="8" fill="#e08d16"/><path d="M4 8l3 3 5-6" stroke="#fff" stroke-width="2" fill="none"/></svg>Größter Kamineinzelhändler Deutschlands</li>
      <li><svg width="16" height="16" viewBox="0 0 16 16"><circle cx="8" cy="8" r="8" fill="#e08d16"/><path d="M4 8l3 3 5-6" stroke="#fff" stroke-width="2" fill="none"/></svg>Garantierter Datenschutz</li>
    </ul>
    <div class="best-price">BESTPREISGARANTIE</div>
    <div class="badges">
      <div class="badge-round"></div>
      <div class="badge-round"></div>
      <div class="badge-wide"></div>
    </div>
    <ul class="trust-list trust-right">
      <li><svg width="16" height="16" viewBox="0 0 16 16"><circle cx="8" cy="8" r="8" fill="#e08d16"/><path d="M4 8l3 3 5-6" stroke="#fff" stroke-width="2" fill="none"/></svg>Kostenlose Fachberatung</li>
      <li><svg width="16" height="16" viewBox="0 0 16 16"><circle cx="8" cy="8" r="8" fill="#e08d16"/><path d="M4 8l3 3 5-6" stroke="#fff" stroke-width="2" fill="none"/></svg>Vorkasse vollständig über Securanta abgesichert</li>
      <li><svg width="16" height="16" viewBox="0 0 16 16"><circle cx="8" cy="8" r="8" fill="#e08d16"/><path d="M4 8l3 3 5-6" stroke="#fff" stroke-width="2" fill="none"/></svg>Sichere Abwicklung und Lieferung</li>
      <li><svg width="16" height="16" viewBox="0 0 16 16"><circle cx="8" cy="8" r="8" fill="#e08d16"/><path d="M4 8l3 3 5-6" stroke="#fff" stroke-width="2" fill="none"/></svg><span>Besuchen Sie unsere Website<small>für weitere Informationen <b>kaminwerk-versand.de</b></small></span></li>
    </ul>
  </section>

  <section class="company-info">
    <div><h3>Anschrift</h3><p>Kaminwerk Versand GmbH<br>Lindenweg 12<br>80331 München</p></div>
    <div><h3>Kontakt</h3><p>info@kaminwerk-versand.de<br>Shop:<br>kaminwerk-versand.de<br>Tel.: 089 4521 3370<br>Fax: 089 4521 3371</p></div>
    <div><h3>Steuernummer</h3><p>USt-ID: DE284517390<br>Finanzamt München<br>Geschäftsführer: M. Keller</p></div>
    <div><h3>Bankverbindung</h3><p>Stadtbank München<br>BLZ 700 400 48<br>Konto 7812 4500<br>IBAN: DE48 7004 0048 7812 4500<br>BIC: STBKDEMMXXX</p></div>
  </section>

  <section class="similar">
    <div class="tabs"><div class="tab tab-active">8358-22</div><div class="tab tab-idle">8358-22</div></div>
    <div class="slide">
      <div class="slide-image" role="img" aria-label="Produktfoto eines Kaminofens mit Sichtfenster"></div>
      <div class="slide-text">
        <h3>Lorem Ipsum is simply dummy</h3>
        <p>Unsere Kaminöfen verbinden zeitloses Design mit moderner Verbrennungstechnik. Jedes Modell wird sorgfältig geprüft und bietet eine gleichmäßige, wohlige Wärme für Ihr Zuhause. Die große Sichtscheibe sorgt für ein eindrucksvolles Flammenbild, während die durchdachte Luftführung die Scheibe lange sauber hält. Dank hochwertiger Materialien und solider Verarbeitung haben Sie viele Jahre Freude an Ihrem Ofen. Unsere Fachberater helfen Ihnen gern bei der Auswahl, der Planung und der fachgerechten Montage, damit Ihr neuer Ofen perfekt zu Ihrem Wohnraum passt.</p>
      </div>
    </div>
    <div class="dots"><i></i><i></i><i></i></div>
  </section>
</main>

<footer class="site-footer">
  <div class="footer-head pay-head">Payment Methods</div>
  <div class="footer-head ship-head">Shipping methods</div>
  <div class="logo-row pay-row"><span>Lastschrift</span><span>Kreditkarte</span><span>Sofortkauf</span><span>Ratenkauf</span><span>Wallet</span><span>Vorkasse</span></div>
  <div class="logo-row ship-row"><span>Paketdienst</span><span>Express</span><span>Spedition</span></div>
  <div class="footer-divider"></div>
  <div class="footer-cols">
    <ul><li>Über uns</li><li>Impressum</li><li>Kontakt</li><li>Karriere</li><li>Blog</li></ul>
    <ul><li>Häufige Fragen</li><li>Widerruf</li><li>Versand</li><li>Bestellstatus</li><li>Zahlung</li></ul>
  </div>
  <div class="support">Support</div>
  <div class="footer-contact"><b>Kostenlose Hotline</b><br>089 4521 3370<br>Mo–Fr 8–18 Uhr<br>info@kaminwerk-versand.de</div>
  <div class="copyright">© 2024 Kaminwerk Versand</div>
</footer>

</body>
</html>
```